Kettlelanternpress: Self-help book needs Promotional Postcard

Need a postcard 8.5" x 5.5" to promote my upcoming book. Its a self-help career book for women focusing on how the mother-daughter relationship impacts careers and tips and solutions for success. The model includes 5 different types of daughters.
Title: Where Did the Quiet Garden Lead Us?
Breathe new life into your career by understanding your mother daughter relationship.
Book release is January 9, 2017
Updates

I just uploaded 5 images of the daughter types without the words, better to use these, thanks! Added Thursday, December 29, 2016

Target Market(s)

This book is targeted towards women

Industry/Entity Type

Promotional

Font styles to use
Serif
Other font styles liked:
• see website text

Colors
00a990
ec252d
e34297

Requirements
Must have
• Eye catching promotional postcard. Must have image of book on front with title and subtitle, author name and website. I'd like images of the 5 daughters on the front.
• Colors should match the cover green and pink
• Back can have quotes and author bio
• can look at website (not quite completed) for more inspiration www.kettlelanternpress.example
Nice to have
• Curious to see how the postcard compliments the book and website.

```html
<!DOCTYPE html>
<html lang="en">
<head>
<meta charset="utf-8">
<title>Where Did the Quiet Garden Lead Us? – Postcard</title>
<link href="https://fonts.googleapis.com/css2?family=Big+Shoulders+Display:wght@300;400&family=Roboto+Condensed:wght@300;400;700&display=swap" rel="stylesheet">
<style>
  :root {
    --ink-black: #000000;
    --rose: #e13a8a;
    --rose-deep: #cf2a78;
    --quote-rose: #d62e6e;
    --cover-green: #a9b98a;
    --cover-green-light: #b9c79c;
    --cover-green-dark: #97a877;
    --cover-pink: #d9286f;
    --cover-ink: #2b2b2b;
    --page-cream: #f1efe6;
    --page-shade: #d9d6c8;
    --white: #ffffff;
    --grey-dot: #cfcfcf;
    --text-dark: #1a1a1a;
  }
  * { margin: 0; padding: 0; box-sizing: border-box; }
  html, body { width: 946px; height: 1200px; overflow: hidden; background: var(--ink-black); }
  body { position: relative; font-family: "Roboto Condensed", sans-serif; }

  .card-front {
    position: absolute; left: 43px; top: 37px; width: 860px; height: 557px;
    background: radial-gradient(ellipse at 40% 40%, #ea4b95 0%, var(--rose) 55%, var(--rose-deep) 100%);
    overflow: hidden;
  }
  .author-line {
    position: absolute; left: 0; width: 518px; top: 52px; text-align: center;
    font-size: 23px; font-weight: 400; color: var(--text-dark);
  }
  .book-title {
    position: absolute; left: 0; width: 518px; top: 97px; text-align: center;
    font-family: "Big Shoulders Display", sans-serif; font-weight: 300;
    font-size: 62px; line-height: 68px; color: var(--white); text-transform: uppercase;
    letter-spacing: 0.5px; text-shadow: 1px 2px 3px rgba(0,0,0,0.25);
  }
  .tagline {
    position: absolute; left: 0; width: 518px; top: 254px; text-align: center;
    font-size: 23px; line-height: 30px; font-weight: 400; color: var(--text-dark);
  }
  .web-button {
    position: absolute; left: 116px; top: 381px; width: 286px; height: 36px;
    border: 1.5px solid #9e1f55; border-radius: 6px;
    background: rgba(160,20,80,0.35);
    display: flex; align-items: center; justify-content: center; gap: 8px;
    font-family: "Big Shoulders Display", sans-serif; font-weight: 400;
    font-size: 21px; color: var(--white);
  }
  .web-button svg { width: 18px; height: 20px; }

  .book-mockup { position: absolute; left: 0; top: 0; width: 860px; height: 557px; }
  .cover-kicker { font-family: "Big Shoulders Display", sans-serif; font-weight: 400; font-size: 21px; letter-spacing: 5px; fill: var(--cover-ink); }
  .cover-hero { font-family: "Big Shoulders Display", sans-serif; font-weight: 400; font-size: 82px; letter-spacing: 2px; fill: var(--cover-pink); }
  .cover-mid { font-family: "Big Shoulders Display", sans-serif; font-weight: 400; font-size: 34px; letter-spacing: 7px; fill: var(--cover-ink); }
  .cover-accent { font-family: "Big Shoulders Display", sans-serif; font-weight: 400; font-size: 40px; letter-spacing: 6px; fill: var(--cover-pink); }
  .cover-mark { font-family: "Big Shoulders Display", sans-serif; font-weight: 400; font-size: 250px; fill: var(--cover-pink); }
  .cover-sub { font-family: "Roboto Condensed", sans-serif; font-weight: 400; font-size: 12.5px; fill: var(--cover-ink); }
  .cover-author { font-family: "Roboto Condensed", sans-serif; font-weight: 400; font-size: 17px; fill: var(--cover-pink); }

  .daughter-figures {
    position: absolute; left: 18px; top: 431px; width: 572px; height: 126px;
    background: linear-gradient(90deg, #1a1a1a 0%, #f2f2f2 15%, #1a1a1a 30%, #f2f2f2 50%, #1a1a1a 70%, #f2f2f2 85%, #1a1a1a 100%);
    clip-path: polygon(0 100%, 2% 10%, 8% 0, 14% 12%, 20% 100%, 22% 30%, 28% 5%, 34% 20%, 40% 100%, 42% 25%, 50% 5%, 56% 25%, 60% 100%, 62% 20%, 70% 8%, 76% 25%, 80% 100%, 82% 15%, 90% 2%, 98% 18%, 100% 100%);
  }

  .card-back-quotes {
    position: absolute; left: 43px; top: 606px; width: 860px; height: 332px;
    background: var(--white);
  }
  .testimonial { position: absolute; left: 100px; width: 660px; text-align: center; }
  .testimonial-text { font-size: 17.5px; line-height: 21px; font-weight: 400; color: var(--quote-rose); }
  .testimonial-source { margin-top: 8px; font-size: 15.5px; line-height: 21px; color: var(--text-dark); }
  .testimonial-source strong { font-weight: 700; }
  .testimonial--first { top: 46px; }
  .testimonial--second { top: 200px; }
  .divider-dots {
    position: absolute; top: 174px; left: 0; width: 860px;
    display: flex; justify-content: center; gap: 9px;
  }
  .divider-dots span { width: 12px; height: 12px; border-radius: 50%; background: var(--grey-dot); }

  .card-back-bio {
    position: absolute; left: 43px; top: 938px; width: 860px; height: 224px;
    background: linear-gradient(180deg, var(--rose-deep) 0%, var(--rose) 100%);
  }
  .author-photo {
    position: absolute; left: 52px; top: -40px; width: 160px; height: 196px;
    border: 3px solid #f2f2f2; border-radius: 14px;
    background: linear-gradient(160deg, #4f6b3a 0%, #8a7a55 50%, #3a2a28 100%);
    transform: rotate(-3deg);
    box-shadow: 0 2px 6px rgba(0,0,0,0.3);
  }
  .author-caption {
    position: absolute; left: 52px; width: 160px; top: 166px; text-align: center;
    font-size: 16px; font-weight: 700; color: var(--white);
  }
  .bio-text {
    position: absolute; left: 235px; top: 18px; width: 556px;
    font-size: 15.3px; line-height: 20.4px; font-weight: 300; color: var(--white);
  }
  .social-line {
    position: absolute; left: 226px; top: 170px;
    font-size: 12.5px; font-weight: 400; color: var(--white);
  }
  .booking-text {
    position: absolute; left: 341px; top: 160px; width: 500px;
    font-size: 14.5px; line-height: 18px; font-weight: 300; color: var(--white);
  }
  .booking-text strong { font-weight: 700; }
</style>
</head>
<body>
  <section class="card-front">
    <p class="author-line">Mara Ellison Quill, M.A, M.ed</p>
    <h1 class="book-title">Where Did the Quiet<br>Garden Lead Us?</h1>
    <p class="tagline">Breathe new life into your career<br>by understanding your<br>Mother-Daughter relationship</p>
    <div class="web-button">
      <svg viewBox="0 0 18 20" aria-hidden="true">
        <path d="M6 2v10l-2-2c-1-1-2.5 0-1.6 1.2L6 16c1 1.5 2 2.5 4 2.5h2c2.5 0 4-1.8 4-4V9c0-1-1.5-1-1.5 0V8c0-1-1.5-1-1.5 0V7.5c0-1-1.5-1-1.5 0V7c0-1-1.5-1-1.5 0V2c0-1.2-2-1.2-2 0z" fill="#fff"/>
      </svg>
      <span>www.kettlelanternpress.example</span>
    </div>

    <svg class="book-mockup" viewBox="0 0 860 557" aria-label="Book: Where Did the Quiet Garden Lead Us? by Mara Ellison Quill">
      <defs>
        <filter id="book-shadow" x="-20%" y="-20%" width="140%" height="140%">
          <feGaussianBlur stdDeviation="10"/>
        </filter>
        <linearGradient id="cover-fill" x1="0" y1="0" x2="1" y2="1">
          <stop offset="0" stop-color="var(--cover-green-light)"/>
          <stop offset="0.6" stop-color="var(--cover-green)"/>
          <stop offset="1" stop-color="var(--cover-green-dark)"/>
        </linearGradient>
      </defs>
      <polygon class="book-shadow" points="512,90 826,70 850,490 545,512" fill="rgba(60,0,25,0.45)" filter="url(#book-shadow)"/>
      <polygon class="book-pages-top" points="503,75 789,53 806,42 520,64" fill="var(--page-cream)"/>
      <polygon class="book-pages-side" points="789,53 806,42 836,466 819,477" fill="var(--page-shade)"/>
      <g class="book-cover" transform="matrix(1,-0.077,0.0708,1,503,75)">
        <rect width="286" height="424" fill="url(#cover-fill)"/>
        <text class="cover-kicker" x="22" y="52">WHERE DID THE</text>
        <text class="cover-hero" x="18" y="138">QUIET</text>
        <text class="cover-mid" x="22" y="186">GARDEN</text>
        <text class="cover-accent" x="22" y="240">LEAD US</text>
        <text class="cover-mark" x="196" y="270">?</text>
        <g transform="rotate(-8 20 340)">
          <text class="cover-sub" x="24" y="316">Breathe New Life Into Your Career</text>
          <text class="cover-sub" x="36" y="331">By Understanding Your</text>
          <text class="cover-sub" x="30" y="346">Mother-Daughter Relationship</text>
          <text class="cover-author" x="28" y="392">Mara Ellison Quill, M.A, M.Ed</text>
        </g>
      </g>
    </svg>

    <div class="daughter-figures" role="img" aria-label="Illustrated profile silhouettes of the five daughter types"></div>
  </section>

  <section class="card-back-quotes">
    <div class="testimonial testimonial--first">
      <p class="testimonial-text">“...Mara draws the reader in with her poignant and insightful perspective of how family dynamics, particularly the conscious and subconscious aspects of the mother/daughter relationship, impact a career path and a fulfilled life...”</p>
      <p class="testimonial-source"><strong>Judge Renata Falcone,</strong> OPEN DOCKET, a syndicated<br>TV court program.</p>
    </div>
    <div class="divider-dots"><span></span><span></span><span></span><span></span></div>
    <div class="testimonial testimonial--second">
      <p class="testimonial-text">“...‘Quiet Garden’ challenges us to pay attention to how we show up at work without assigning blame or judgement. Mara draws on decades of career counseling to provide knowledgeable insight and practical tips, wrapped in a warm hug…”</p>
      <p class="testimonial-source"><strong>Delia M Hart,</strong> Executive Women's Leadership and Mindfulness Coach.</p>
    </div>
  </section>

  <section class="card-back-bio">
    <div class="author-photo" role="img" aria-label="Portrait photograph of the author outdoors"></div>
    <p class="author-caption">Mara Ellison Quill</p>
    <p class="bio-text">Mara Ellison Quill, M.A., M.Ed. is a clinical career counselor and licensed mental health counselor who has been helping clients make meaningful career transitions and address workplace challenges for over 26 years. She is the 2013 recipient of the Outstanding Career Practitioner Award from the National Career Guidance Society. 'Quiet Garden' integrates her expertise in career development with her training and insight about the adult mother-daughter relationship.</p>
    <p class="social-line">Kettlelanternpress</p>
    <p class="booking-text">To Book Mara for a speaking event, please contact her at <strong>555 014-2290</strong> or visit <strong>www.kettlelanternpress.example</strong> for more information.</p>
  </section>
</body>
</html>
```